Velora "Glass Tide" single cover

We need a cover for Velora's New upcoming single "Glass Tide"
We have posted some Pictures and logo that we want you to work With. We need you to get her to look good :).The title is "Glass Tide" and is "Velora feat. Dorvo mint rascal"
The songs is a little hiphop/RnB (Marla Q'ish).
You can choose what colour you want for the logo and overall. But we don't want it to be gloomy.
watch www.velora-music.example or www.facebook.com/veloramusic
This is a digital release so we need only front page 12x12cm
Updates
If anyone wants to remove the background from the pictures and be creative that is fine! :)
Industry/Entity Type
Digital
Colors
Designer to choose colors to be used in the design.
Look and feel
Each slider illustrates characteristics of the customer's brand and the style your logo design should communicate.

```html
<!DOCTYPE html>
<html lang="en">
<head>
<meta charset="utf-8">
<title>Velora – Glass Tide</title>
<link rel="stylesheet" href="https://fonts.googleapis.com/css2?family=Permanent+Marker&family=Poiret+One&display=swap">
<style>
  :root {
    --paper: #ffffff;
    --brick: #b4553b;
    --brick-deep: #87392a;
    --shade: #241d1c;
    --sky-grey: #a3acb6;
    --wall-light: #dde1e5;
    --artist-orange: #f39200;
    --credit-pink: #ec5f9c;
  }
  html, body {
    margin: 0;
    padding: 0;
    width: 1200px;
    height: 1200px;
    overflow: hidden;
    background: var(--paper);
  }
  .cover {
    position: relative;
    width: 1200px;
    height: 1200px;
    background: var(--paper);
    font-family: "Poiret One", sans-serif;
  }
  .title-block {
    position: absolute;
    left: 0;
    top: 80px;
    width: 1200px;
    height: 830px;
    display: block;
  }
  .title-word {
    font-family: "Permanent Marker", cursive;
    font-size: 430px;
    fill: var(--paper);
  }
  .artist-name {
    position: absolute;
    left: 0;
    width: 1200px;
    top: 905px;
    margin: 0;
    text-align: center;
    font-size: 74px;
    font-weight: 400;
    line-height: 1;
    color: var(--artist-orange);
    letter-spacing: 2px;
    text-transform: lowercase;
  }
  .credits {
    position: absolute;
    left: 0;
    width: 1200px;
    top: 988px;
    margin: 0;
    text-align: center;
    color: var(--credit-pink);
    font-size: 52px;
    font-weight: 400;
    line-height: 58px;
    letter-spacing: 2px;
    text-transform: uppercase;
  }
  .credits span { display: block; }
</style>
</head>
<body>
  <main class="cover">
    <svg class="title-block" viewBox="0 0 1200 830" xmlns="http://www.w3.org/2000/svg">
      <defs>
        <linearGradient id="photo-tones" x1="0" y1="0" x2="1" y2="0">
          <stop offset="0" stop-color="#b4553b"/>
          <stop offset="0.25" stop-color="#87392a"/>
          <stop offset="0.42" stop-color="#241d1c"/>
          <stop offset="0.62" stop-color="#241d1c"/>
          <stop offset="0.72" stop-color="#87392a"/>
          <stop offset="0.84" stop-color="#a3acb6"/>
          <stop offset="1" stop-color="#dde1e5"/>
        </linearGradient>
      </defs>
      <path class="photo-area" role="img"
            aria-label="Photo of the artist sitting against a brick wall, showing through the brushed title"
            fill="url(#photo-tones)"
            d="M60 70 Q300 40 560 30 Q800 20 1140 60 Q1170 300 1150 560 Q1130 720 1080 810 Q700 830 400 815 Q150 800 40 780 Q20 500 30 260 Q35 120 60 70 Z"/>
      <text class="title-word" x="600" y="400" text-anchor="middle"
            textLength="1080" lengthAdjust="spacingAndGlyphs"
            transform="rotate(-3 600 400)">GLASS</text>
      <text class="title-word" x="610" y="780" text-anchor="middle"
            textLength="900" lengthAdjust="spacingAndGlyphs"
            transform="rotate(-2 610 780)">TIDE</text>
    </svg>
    <h1 class="artist-name">Velora</h1>
    <p class="credits">
      <span class="credits-feature">Feat Dorvo Mint Rascal</span>
      <span class="credits-title">Glass Tide</span>
    </p>
  </main>
</body>
</html>
```